Silver Heron Staffing Agency

I need to make a brochure/catalogue that represent our company, telling our clients what we do, our values, fields of industry that we taken care of, so they know who we are, what we did, and how we do it.
I do have a logo and simple brochure design before that i really need to upgrade (i will give it as an example on this attachment).

What I want in the new design is :
1. More pictures and little bit of explanation in each industry we work with.
2. Attractive design that make people LOOK at the brochure and not just throw it in the trash.
3. Still use the combination color of the company logo itself, which is Golden Brown.

```html
<!DOCTYPE html>
<html lang="en">
<head>
<meta charset="utf-8">
<title>Silver Heron Staffing Agency – Trifold Brochure</title>
<link href="https://fonts.googleapis.com/css2?family=Open+Sans:wght@400;600;700;800&display=swap" rel="stylesheet">
<style>
:root{
  --gold:#b8913f;
  --gold-light:#d4b26a;
  --ink:#151515;
  --paper:#ffffff;
  --bg:#e4e4e4;
  --text:#3a3a3a;
  --text-light:#d6d6d6;
}
*{box-sizing:border-box;margin:0;padding:0}
html,body{width:1200px;height:2400px;overflow:hidden}
body{background:var(--bg);font-family:"Open Sans",Arial,sans-serif;color:var(--text);position:relative}
.spread{position:absolute;left:30px;width:1140px;height:880px;display:flex;box-shadow:0 10px 30px rgba(0,0,0,.18)}
.spread--outside{top:240px}
.spread--inside{top:1280px}
.panel{position:relative;width:380px;height:880px;overflow:hidden;background:var(--paper)}
.panel--dark{background:var(--ink);color:var(--text-light)}
.footer-bar{position:absolute;left:0;right:0;bottom:0;height:34px;background:var(--gold);display:flex;align-items:center;padding-left:22px;gap:8px;font-size:11px;color:#fff;font-weight:600}
.footer-bar .dot{width:12px;height:12px;border-radius:50%;border:1.5px solid #fff}
.brand{font-weight:700;color:var(--gold);font-size:18px;letter-spacing:.5px;text-align:center;line-height:1.2}
.p{font-size:10.5px;line-height:1.55}
.h-gold{color:var(--gold);font-weight:800;font-size:17px;letter-spacing:.5px}
.h-dark{color:var(--ink);font-weight:800;font-size:17px}
.sub{color:var(--gold);font-weight:700;font-size:11px;margin-bottom:2px}
.underline{display:block;width:46px;height:3px;background:var(--gold);margin-top:4px}

/* flap: industries */
.flap .team-photo{position:absolute;left:0;top:0;width:380px;height:240px;background:linear-gradient(160deg,#c9cdd2,#6e6a66)}
.flap .gold-rule{position:absolute;left:0;top:240px;width:380px;height:8px;background:var(--gold)}
.flap .lead{position:absolute;left:26px;top:268px;width:330px;font-size:14px;font-weight:800;color:var(--ink);line-height:1.3}
.flap .lead span{color:var(--gold)}
.flap .intro{position:absolute;left:26px;top:312px;width:330px}
.industries{position:absolute;left:22px;top:392px;width:340px;display:grid;grid-template-columns:1fr 1fr;row-gap:14px;column-gap:12px;list-style:none}
.industry{display:flex;gap:8px;align-items:flex-start}
.industry__photo{width:42px;height:42px;border-radius:50%;border:2px solid var(--gold);flex:none}
.industry__name{font-size:11.5px;font-weight:700;color:var(--ink);line-height:1.2;margin-bottom:2px}
.industry__text{font-size:9.5px;line-height:1.4;color:var(--text)}

/* back panel */
.back .circle-photo{position:absolute;left:95px;top:40px;width:190px;height:190px;border-radius:50%;border:5px solid var(--gold);background:linear-gradient(140deg,#efe9e2,#a99c8d)}
.back .tag{position:absolute;left:100px;top:218px;width:180px;height:34px;background:var(--gold);color:var(--ink);font-weight:800;font-size:14px;display:flex;align-items:center;justify-content:center}
.back .text1{position:absolute;left:34px;top:286px;width:312px}
.back .text2{position:absolute;left:34px;top:390px;width:312px}
.back .brand{position:absolute;left:0;right:0;top:540px;font-size:20px}
.back .contact{position:absolute;left:0;right:0;top:610px;text-align:center;font-size:11px;line-height:1.7}

/* cover */
.cover .brand-wrap{position:absolute;left:0;right:0;top:60px;display:flex;flex-direction:column;align-items:center;gap:6px}
.cover .brand-wrap .sq{width:14px;height:14px;background:var(--gold)}
.cover .hero{position:absolute;left:0;top:170px;width:380px;height:470px;background:linear-gradient(160deg,#b9a58a,#7b634a 60%,#4b4038)}
.cover .band{position:absolute;left:0;top:500px;width:380px}
.cover .slogan{position:absolute;left:40px;top:660px;width:300px;color:var(--gold);font-weight:800;font-size:32px;line-height:1.15;text-align:center;letter-spacing:.5px}

/* inside left */
.about .block{position:absolute;left:28px;width:324px}
.about .h-gold{display:flex;align-items:center;gap:10px;margin-bottom:8px}
.about .icon{width:22px;height:22px;flex:none}

/* inside middle */
.services .block{position:absolute;left:28px;width:324px}
.services .circle-photo{position:absolute;left:105px;top:360px;width:170px;height:170px;border-radius:50%;border:5px solid var(--gold);background:linear-gradient(140deg,#cfd6c9,#7f8b6d)}
.services .save{position:absolute;left:90px;top:500px;width:200px;background:var(--ink);color:#fff;text-align:center;font-size:12px;font-weight:700;padding:6px 0;border-bottom:4px solid var(--gold)}
.services .save b{color:var(--gold)}

/* inside right */
.values .brand-wrap{position:absolute;left:0;right:0;top:34px;display:flex;flex-direction:column;align-items:center;gap:6px}
.values .brand-wrap .sq{width:12px;height:12px;background:var(--gold)}
.values .block{position:absolute;left:28px;width:324px}
.values .gold-box{position:absolute;left:0;top:310px;width:380px;height:230px;background:var(--gold);padding:22px 28px;color:#fff}
</style>
</head>
<body>

<section class="spread spread--outside">
  <article class="panel flap">
    <div class="team-photo" role="img" aria-label="Photo of job candidates seated in a row waiting for interviews"></div>
    <div class="gold-rule"></div>
    <h2 class="lead"><span>WE FIND</span> THE BEST PEOPLE FOR THE FOLLOWING INDUSTRIES</h2>
    <p class="p intro">Our success is based on our unique ability to identify top candidates and the high quality professional development of our people, matched to the needs of every client.</p>
    <ul class="industries">
      <li class="industry">
        <div class="industry__photo" style="background:linear-gradient(135deg,#c9a56a,#6b5434)" role="img" aria-label="Photo of warehouse workers moving stock"></div>
        <div><div class="industry__name">Warehousing</div><p class="industry__text">Pickers, packers and forklift operators ready for any shift.</p></div>
      </li>
      <li class="industry">
        <div class="industry__photo" style="background:linear-gradient(135deg,#9aa6b2,#4a525c)" role="img" aria-label="Photo of a delivery truck driver"></div>
        <div><div class="industry__name">Transportation</div><p class="industry__text">Licensed drivers and dock crews keeping freight moving.</p></div>
      </li>
      <li class="industry">
        <div class="industry__photo" style="background:linear-gradient(135deg,#e0cdb0,#8a6f50)" role="img" aria-label="Photo of hotel staff greeting guests"></div>
        <div><div class="industry__name">Hospitality</div><p class="industry__text">Friendly hotel, event and front desk staff on demand.</p></div>
      </li>
      <li class="industry">
        <div class="industry__photo" style="background:linear-gradient(135deg,#a8bf8a,#4f6a3a)" role="img" aria-label="Photo of landscapers tending a garden"></div>
        <div><div class="industry__name">Landscaping</div><p class="industry__text">Seasonal crews for lawn care, planting and upkeep.</p></div>
      </li>
      <li class="industry">
        <div class="industry__photo" style="background:linear-gradient(135deg,#c8d0d6,#6c7880)" role="img" aria-label="Photo of a cleaner working in an office"></div>
        <div><div class="industry__name">Janitorial</div><p class="industry__text">Reliable cleaners for offices, plants and public sites.</p></div>
      </li>
      <li class="industry">
        <div class="industry__photo" style="background:linear-gradient(135deg,#e3c08a,#9a5f34)" role="img" aria-label="Photo of food handlers in a kitchen"></div>
        <div><div class="industry__name">Food Handling</div><p class="industry__text">Trained kitchen and line workers who follow safe practice.</p></div>
      </li>
      <li class="industry">
        <div class="industry__photo" style="background:linear-gradient(135deg,#ddd3c2,#8d7f6a)" role="img" aria-label="Photo of workers sorting paper mail"></div>
        <div><div class="industry__name">Paper Mailing</div><p class="industry__text">Sorting, folding and inserting teams for mail rooms.</p></div>
      </li>
      <li class="industry">
        <div class="industry__photo" style="background:linear-gradient(135deg,#cfae7e,#7a5a36)" role="img" aria-label="Photo of workers packing boxes on a line"></div>
        <div><div class="industry__name">Packaging</div><p class="industry__text">Fast, careful hands for labeling and boxing lines.</p></div>
      </li>
    </ul>
    <div class="footer-bar"><span class="dot"></span>www.silverheronstaffing.com</div>
  </article>

  <article class="panel panel--dark back">
    <div class="circle-photo" role="img" aria-label="Photo of a caregiver assisting a patient"></div>
    <div class="tag">Contract To Hire</div>
    <p class="p text1">Reduce the risk of making a bad hire by evaluating a candidate's performance in your own environment. You can choose to add workers to your permanent team or request another worker for your evaluation.</p>
    <p class="p text2">With more than 10 years of experience, Silver Heron Staffing has provided staffing services throughout New Jersey, New York, Pennsylvania, Delaware, Virginia and Georgia.</p>
    <div class="brand">Silver Heron Inc</div>
    <div class="contact">555 014 2290<br>42 Maple Ave, Ste 8<br>Rivertown, NJ 08000<br>hello@silverheronstaffing.com<br>www.silverheronstaffing.com</div>
    <div class="footer-bar"><span class="dot"></span>www.silverheronstaffing.com</div>
  </article>

  <article class="panel cover">
    <div class="brand-wrap"><span class="sq"></span><div class="brand">Silver Heron Inc</div></div>
    <div class="hero" role="img" aria-label="Photo of a smiling warehouse worker in a hard hat carrying cardboard boxes"></div>
    <svg class="band" width="380" height="346" viewBox="0 0 380 346" aria-hidden="true">
      <defs><linearGradient id="bandFade" x1="0" y1="0" x2="0" y2="1"><stop offset="0" stop-color="#2b2b2b"/><stop offset="1" stop-color="#0e0e0e"/></linearGradient></defs>
      <polygon points="0,70 380,0 380,346 0,346" fill="url(#bandFade)"/>
      <polygon points="0,60 380,-10 380,0 0,70" fill="#b8913f"/>
    </svg>
    <h1 class="slogan">YOUR BEST WAY TO SUCCEED</h1>
    <div class="footer-bar"><span class="dot"></span>www.silverheronstaffing.com</div>
  </article>
</section>

<section class="spread spread--inside">
  <article class="panel panel--dark about">
    <div class="block" style="top:40px">
      <h2 class="h-gold">ABOUT US</h2>
      <p class="p">Our ethics are a crucial building block of our business. Our own mission is based on adherence to the highest ethical standards. Together, these relationships give us the ability to identify top candidates and deliver quality professionals to every client we serve.</p>
    </div>
    <div class="block" style="top:220px">
      <h2 class="h-gold"><svg class="icon" viewBox="0 0 22 22"><circle cx="7" cy="8" r="3" fill="#b8913f"/><circle cx="15" cy="8" r="3" fill="#b8913f"/><path d="M2 19c0-4 3-6 5-6s5 2 5 6M10 19c0-4 3-6 5-6s5 2 5 6" fill="#b8913f"/></svg>CULTURE</h2>
      <p class="p">Silver Heron believes in equal opportunity for all regardless of gender, race, age, religion or background. We treat our workers and clients with respect, and we are committed to building a supportive team culture and long lasting relationships.</p>
    </div>
    <div class="block" style="top:420px">
      <h2 class="h-gold"><svg class="icon" viewBox="0 0 22 22"><circle cx="11" cy="11" r="9" fill="none" stroke="#b8913f" stroke-width="2"/><circle cx="11" cy="11" r="4" fill="#b8913f"/></svg>MISSION</h2>
      <p class="p">Silver Heron is more than a staffing company; we want to become your business partner. We understand that payroll and employee services are a major part of your operation, and we take that responsibility off your hands so you can focus on growth and results.</p>
    </div>
    <div class="block" style="top:640px">
      <h2 class="h-gold"><svg class="icon" viewBox="0 0 22 22"><rect x="3" y="3" width="16" height="16" rx="2" fill="none" stroke="#b8913f" stroke-width="2"/><path d="M7 11l3 3 5-6" fill="none" stroke="#b8913f" stroke-width="2"/></svg>OUR PROCESS</h2>
      <p class="p">Our screening process includes a thorough interview with each potential candidate to give us insight into their skills, previous work history and career goals, as well as reference checks with their previous employers.</p>
    </div>
    <div class="footer-bar"><span class="dot"></span>www.silverheronstaffing.com</div>
  </article>

  <article class="panel services">
    <div class="block" style="top:36px">
      <h2 class="h-dark">OUR <span style="color:var(--gold)">SERVICES</span><span class="underline"></span></h2>
    </div>
    <div class="block" style="top:90px">
      <div class="sub">Employee Payroll</div>
      <p class="p">Employees are paid on a weekly basis. Our system ensures that all taxes and deductions are handled accurately and on time.</p>
    </div>
    <div class="block" style="top:170px">
      <div class="sub">Workers Compensation</div>
      <p class="p">We provide workers compensation for our employees. If an injury occurs, we handle all claims so your business stays protected and running smoothly.</p>
    </div>
    <div class="block" style="top:262px">
      <div class="sub">Safety Training</div>
      <p class="p">Every worker receives safety orientation before placement on your site.</p>
    </div>
    <div class="circle-photo" role="img" aria-label="Photo of a smiling professional woman in an office"></div>
    <div class="save">We Save you both<br><b>TIME and MONEY</b></div>
    <div class="block" style="top:560px">
      <p class="p">Contact us today to start a new partnership and see the results for yourself.</p>
    </div>
    <div class="block" style="top:610px">
      <h2 class="h-dark">WHY <span style="color:var(--gold)">STAFFING?</span><span class="underline"></span></h2>
    </div>
    <div class="block" style="top:660px">
      <div class="sub">Avoid Unemployment Costs</div>
      <p class="p">Temporary staff are employees of the agency, so you avoid unemployment claims and related costs when projects end.</p>
    </div>
    <div class="block" style="top:740px">
      <div class="sub">Flexibility</div>
      <p class="p">Scale your workforce up or down as demand changes, without long term commitments.</p>
    </div>
    <div class="footer-bar"><span class="dot"></span>www.silverheronstaffing.com</div>
  </article>

  <article class="panel values">
    <div class="brand-wrap"><span class="sq"></span><div class="brand" style="font-size:15px">Silver Heron Inc</div></div>
    <div class="block" style="top:110px">
      <div class="sub">Reliable Workforce</div>
      <p class="p">Our temporary staff has proven to be reliable and ready to work. We are available around the clock to meet your staffing needs, and we match each worker to the role that fits them best.</p>
    </div>
    <div class="block" style="top:210px">
      <p class="p">Our success is built on a strong foundation of trust. We work closely with each client to understand their goals and deliver dependable people.</p>
    </div>
    <div class="gold-box">
      <p class="p">We believe that knowledge is a strong factor in staffing success. Our experience across many industries gives us a clear view of what each client needs and how to meet it quickly.</p>
      <p class="p" style="margin-top:12px">When you are looking for a qualified candidate or when you need a new job, Silver Heron Staffing is the right partner. Together we reach your goals faster.</p>
    </div>
    <div class="block" style="top:570px">
      <div class="sub">Increased Productivity</div>
      <p class="p">Temporary employees can be brought in to cover peak seasons, special projects or absences, keeping your permanent team focused and productive.</p>
    </div>
    <div class="block" style="top:680px">
      <div class="sub">Reduced Overtime</div>
      <p class="p">Employing temporary staff lowers overtime costs and prevents burnout among your regular employees, saving you money every week.</p>
    </div>
    <div class="footer-bar"><span class="dot"></span>www.silverheronstaffing.com</div>
  </article>
</section>

</body>
</html>
```